Kem7Dex Letterhead

Need a new letterhead for my law firm.
IDENTIFYING INFORMATION BELOW:
Ansel T Brightwater III
Attorney at Law
Address: 4832 Tillbury Rd, Ste 250, Dallas, TX 75204
Phone: 866-402-7183
Fax: 469-583-0271
Email: kem@kem7dex.example
Website: www.kem7dex.example

Colors
0054AA
0677BA
7BADD7
CADEEF
E8F1F8

Requirements
Must have
• Logo needs to be on the letterhead, along with identifying information which is included in the project description.

```html
<!DOCTYPE html>
<html lang="en">
<head>
<meta charset="utf-8">
<title>Kem7Dex Letterhead</title>
<link rel="stylesheet" href="https://fonts.googleapis.com/css2?family=Montserrat:wght@800&family=Inter:ital,wght@0,400;0,700;1,400&family=Great+Vibes&display=swap">
<style>
  :root {
    --ink: #111111;
    --navy: #0054AA;
    --blue: #2f6bf0;
    --sky: #7BADD7;
    --mist: #CADEEF;
    --panel: #f3fafd;
    --muted: #a9a9a9;
    --white: #ffffff;
  }
  * { margin: 0; padding: 0; box-sizing: border-box; }
  html, body { width: 848px; height: 1200px; overflow: hidden; background: var(--white); }
  .letterhead {
    position: relative; width: 848px; height: 1200px;
    font-family: "Inter", Arial, sans-serif; color: var(--ink);
  }
  .brand {
    position: absolute; left: 51px; top: 44px;
    font-family: "Montserrat", Arial, sans-serif; font-weight: 800;
    font-size: 40px; letter-spacing: 1.5px; color: var(--ink);
  }
  .header-rule {
    position: absolute; left: 0; top: 120px; width: 480px; height: 8px;
    background: linear-gradient(90deg, var(--blue) 0%, var(--sky) 60%, rgba(202,222,239,0) 100%);
  }
  .wave-art {
    position: absolute; left: 475px; top: 68px; width: 373px; height: 68px;
    background: linear-gradient(90deg, rgba(202,222,239,0.5) 0%, var(--sky) 35%, #3d8ee6 65%, var(--blue) 100%);
    border-radius: 34px 0 0 34px; opacity: 0.85;
  }
  .sheet {
    position: absolute; left: 84px; top: 179px; width: 680px; height: 858px;
    background: var(--panel);
  }
  .recipient {
    position: absolute; left: 51px; top: 33px; font-size: 16.5px; line-height: 20.5px;
  }
  .recipient .name { font-weight: 700; }
  .recipient .role { font-style: italic; }
  .body-copy {
    position: absolute; left: 49px; top: 139px; width: 600px;
    font-size: 16.3px; line-height: 20.5px;
  }
  .body-copy p + p { margin-top: 20.5px; }
  .signature {
    position: absolute; left: 49px; top: 700px; width: 184px;
    border-bottom: 1.5px solid var(--ink); padding-bottom: 4px;
    font-family: "Great Vibes", cursive; font-size: 28px; line-height: 36px;
  }
  .signer { position: absolute; left: 51px; top: 757px; font-size: 16.5px; line-height: 21px; }
  .signer .name { font-weight: 700; }
  .signer .role { font-style: italic; }
  .brand-small {
    position: absolute; left: 51px; top: 812px;
    font-family: "Montserrat", Arial, sans-serif; font-weight: 800;
    font-size: 16px; color: var(--muted); letter-spacing: 0.5px;
  }
  .footer-rule {
    position: absolute; left: 0; top: 1081px; width: 848px; height: 8px;
    background: linear-gradient(90deg, var(--blue) 0%, var(--sky) 65%, var(--mist) 100%);
  }
  .contact {
    position: absolute; top: 1104px; left: 80px; right: 56px; height: 34px;
    display: flex; justify-content: space-between; align-items: center;
    font-size: 11px; white-space: nowrap;
  }
  .contact-item { display: flex; align-items: center; gap: 8px; }
  .contact-item svg { width: 17px; height: 17px; flex: none; }
  .contact-item span { line-height: 14px; }
</style>
</head>
<body>
<div class="letterhead">
  <div class="brand">KEM7DEX</div>
  <div class="header-rule"></div>
  <div class="wave-art" role="img" aria-label="Decorative blue ocean wave flourish"></div>

  <main class="sheet">
    <div class="recipient">
      <div>To</div>
      <div class="name">Marlow Kestrel</div>
      <div class="role">Client</div>
    </div>
    <div class="body-copy">
      <p>Tem esenistis nectur, conemqui conserfero cus parcidi gnatius et hiti sum que veniminvent odis etum faceped quae ne sitis deligendebis pro mint odit, quiam fugit aut landaes tibus, sa volorat adi officaborum que cum et aceario repudan iaspict aquibus.</p>
      <p>Ari aut facesequae dolupta tiurero ipis quo quia voluptae eum diciandus<br>ut quasperio voluptat aut esequam quate cus, commodit, qui aut molo que sedigeni doluptur atende sint, qui aut liate nim nostrum delitem fugiatus</p>
      <p>maiorep raepeditam voluptatus rest eos dis rescia voluptatquam faccaepe voluptaero mo omniet voluptateste porehen tiores num ut voluptis et erum nimus dicae conse magnimp oribus del minis acculpa necaborit paruptatur antibus cum apistis sunt inullam, sint oditat quam ea nus.<br>Am, offictotae pore pliquia nonsed mo cus aut era dolorpore doluptatem es natur?</p>
      <p>Onseculpa doluptae consequae repellat fugiametur reria nonsequunda con resed quatur sequid quiaepudae num vit, consequam estemodi soloribmag-nihil in prae porerion estio. Udiores et videles equibustis aliquis con eicit dent lat explic te nus is ut ea vitio magnihil ipsuntianda dolorem dolorep eliata arum landion coremporpor anderibus, nullentur sa suntus experrum et et abores es dis molupta tureces aut et, consectet expe est, ut aut quo velitate earupicae natem quia volor aut mos ab in res eum nobis esto doluptatquas ant.</p>
    </div>
    <div class="signature">Digital Signature</div>
    <div class="signer">
      <div class="name">Ansel T Brightwater III</div>
      <div class="role">Attorney at Law</div>
    </div>
    <div class="brand-small">KEM7DEX</div>
  </main>

  <div class="footer-rule"></div>
  <footer class="contact">
    <div class="contact-item">
      <svg viewBox="0 0 24 24"><path d="M6 2l4 5-2 3c1 3 3 5 6 7l3-2 5 4-3 4C10 22 2 14 3 5z" fill="var(--ink)"/></svg>
      <span>866-402-7183</span>
    </div>
    <div class="contact-item">
      <svg viewBox="0 0 24 24"><rect x="6" y="2" width="12" height="7" fill="none" stroke="var(--ink)" stroke-width="2"/><rect x="2" y="9" width="20" height="12" rx="2" fill="var(--ink)"/><rect x="7" y="13" width="10" height="4" fill="var(--white)"/></svg>
      <span>469-583-0271</span>
    </div>
    <div class="contact-item">
      <svg viewBox="0 0 24 24"><rect x="2" y="5" width="20" height="14" fill="var(--ink)"/><path d="M2 5l10 8 10-8" fill="none" stroke="var(--white)" stroke-width="1.5"/></svg>
      <span>kem@kem7dex.example</span>
    </div>
    <div class="contact-item">
      <svg viewBox="0 0 24 24" fill="none" stroke="var(--ink)" stroke-width="1.6"><circle cx="12" cy="12" r="10"/><ellipse cx="12" cy="12" rx="4.5" ry="10"/><path d="M2 12h20M4 7h16M4 17h16"/></svg>
      <span>www.kem7dex.example</span>
    </div>
    <div class="contact-item">
      <svg viewBox="0 0 24 24"><path d="M12 2a7 7 0 0 0-7 7c0 5 7 12 7 12s7-7 7-12a7 7 0 0 0-7-7z" fill="var(--ink)"/><circle cx="12" cy="9" r="2.6" fill="var(--white)"/><ellipse cx="12" cy="22" rx="7" ry="1.5" fill="none" stroke="var(--ink)" stroke-width="1.2"/></svg>
      <span>4832 Tillbury Rd, Ste<br>250, Dallas, TX 75204</span>
    </div>
  </footer>
</div>
</body>
</html>
```